NovaLumaro Unique Gift Certificate

We need a unique, luxury gift certificate created for our online company (NovaLumaro). We are looking for something out of the ordinary, ie. do not want it to look like a 'normal' gift certificate. Please visit our website to gain a feel for our company (novalumaro.com.au). The dimensions are 148x148mm. We need our logo, website details, to, from, description, code, exp date included. The certificate will be printed on wood veneer so watermarks will not work. We want it to be clean and minimalistic.

Industry/Entity Type

It Company

```html
<!DOCTYPE html>
<html lang="en">
<head>
<meta charset="utf-8">
<title>NovaLumaro Gift Certificate</title>
<link rel="stylesheet" href="https://fonts.googleapis.com/css2?family=Open+Sans:wght@400;600&family=Cabin+Sketch:wght@700&display=swap">
<style>
  :root {
    --backdrop: #4a3328;
    --veneer-light: #f8ecc4;
    --veneer-mid: #f1dca6;
    --veneer-warm: #e9c98c;
    --brand-blue: #3a9fc4;
    --brand-blue-light: #8fd0e8;
    --ink: #2d2a26;
    --muted: #8a8478;
    --white: #ffffff;
  }
  * { margin: 0; padding: 0; box-sizing: border-box; }
  html, body {
    width: 1200px; height: 750px; overflow: hidden;
    background: var(--backdrop);
  }
  .canvas {
    position: relative; width: 1200px; height: 750px;
    display: flex; align-items: center; justify-content: center;
  }
  .certificate {
    position: relative; width: 660px; height: 660px;
    box-shadow: 0 10px 30px rgba(0,0,0,.35);
  }
  .veneer {
    position: absolute; inset: 0;
    background:
      radial-gradient(ellipse 18% 40% at 22% 55%, var(--veneer-warm), transparent 70%),
      radial-gradient(ellipse 16% 35% at 78% 40%, var(--veneer-warm), transparent 70%),
      linear-gradient(90deg, var(--veneer-light), var(--veneer-mid) 50%, var(--veneer-light));
  }
  .artwork { position: absolute; inset: 0; }
  .brand-name {
    font-family: "Open Sans", sans-serif; font-weight: 600;
    font-size: 34px; fill: var(--ink);
  }
  .tagline {
    font-family: "Open Sans", sans-serif; font-size: 13px;
    letter-spacing: 0.5px; fill: var(--ink);
  }
  .title {
    font-family: "Cabin Sketch", cursive; font-weight: 700; font-size: 62px;
    fill: var(--brand-blue-light); stroke: var(--brand-blue); stroke-width: 1.2;
  }
  .field-label {
    font-family: "Open Sans", sans-serif; font-size: 17px; fill: var(--ink);
  }
  .field-line { stroke: var(--ink); stroke-width: 1.6; stroke-dasharray: 1.5 3.5; }
  .code-label {
    font-family: "Open Sans", sans-serif; font-size: 20px; letter-spacing: 1px; fill: var(--muted);
  }
  .web-address {
    font-family: "Open Sans", sans-serif; font-size: 20px; fill: var(--white);
  }
</style>
</head>
<body>
<main class="canvas">
  <section class="certificate">
    <div class="veneer" role="img" aria-label="Light pine wood veneer grain"></div>
    <svg class="artwork" viewBox="0 0 660 660" width="660" height="660">
      <g class="frame" fill="none" stroke="var(--brand-blue)" stroke-width="6">
        <polyline points="230,50 45,50 45,615 590,615"/>
        <polyline points="440,58 615,58 615,540"/>
        <line x1="600" y1="615" x2="605" y2="615"/>
      </g>

      <circle class="brand-circle" cx="330" cy="130" r="68" fill="none" stroke="var(--brand-blue)" stroke-width="6"/>
      <text class="brand-name" x="330" y="238" text-anchor="middle">NovaLumaro</text>
      <text class="tagline" x="330" y="263" text-anchor="middle">Discover • Connect • Grow</text>

      <text class="title" x="330" y="335" text-anchor="middle">Gift Certificate</text>
      <g class="title-rule" fill="var(--muted)">
        <rect x="140" y="354" width="6" height="6"/>
        <rect x="146" y="356" width="368" height="2"/>
        <rect x="514" y="354" width="6" height="6"/>
      </g>

      <g class="fields">
        <text class="field-label" x="80" y="405">To.</text>
        <line class="field-line" x1="108" y1="405" x2="495" y2="405"/>
        <text class="field-label" x="80" y="445">From.</text>
        <line class="field-line" x1="128" y1="445" x2="495" y2="445"/>
        <text class="field-label" x="80" y="485">Description.</text>
        <line class="field-line" x1="180" y1="485" x2="495" y2="485"/>
        <text class="field-label" x="80" y="525">Exp. Date.</text>
        <line class="field-line" x1="164" y1="525" x2="495" y2="525"/>
      </g>

      <polygon class="code-tab" points="512,375 537,398 562,375 562,580 512,580" fill="var(--veneer-light)" stroke="var(--brand-blue)" stroke-width="6"/>
      <text class="code-label" transform="translate(545,520) rotate(-90)">CODE</text>

      <polygon class="web-banner" points="22,538 640,552 640,602 40,588 52,562" fill="var(--brand-blue)"/>
      <g class="globe-icon" fill="none" stroke="var(--white)" stroke-width="1.6">
        <circle cx="208" cy="569" r="9"/>
        <ellipse cx="208" cy="569" rx="4" ry="9"/>
        <line x1="199" y1="569" x2="217" y2="569"/>
      </g>
      <text class="web-address" x="226" y="576">www.novalumaro.com.au</text>
    </svg>
  </section>
</main>
</body>
</html>
```